Clearing a Court Debt Mark - Banner Ad for TR Website

I need a banner ad for a book I'm selling.

The book is about Clearing a Court Debt Mark, that is a County Court Judgment, from a credit report.

I have two websites. I want the banner ad to appear on
www.thornridgelaw.co.uk

It will then link to the new site: https://clearyourrecordguide.co.uk/

The first site already has a lot of traffic from visitors wanting to remove a CCJ. The purpose of that first site was originally for visitors to become clients of the law firm. However, most visitors can't afford legal advice and so I'd like to offer them the book instead.

I would like to see designs that use the colour green. The final design should communicate financial freedom, simplicity and trustworthiness.

Target Market(s)

Individuals who have discovered a CCJ on their credit report

Industry/Entity Type

Law

Font styles to use
Sans Serif

Colors
0054AA
0677BA
7BADD7
CADEEF
E8F1F8
0094D4
00A9DD
6FCCEA
C7EBF8
E9F6FB
00AB8E
00BBA5
67D7C9
C6EFE9
E9F9F6

Requirements
Must have
• Must fit at the end of a blog article, such as this one https://www.thornridgelaw.co.uk/ccj-wrong-address/

```html
<!DOCTYPE html>
<html lang="en">
<head>
<meta charset="utf-8">
<title>Clearing a Court Debt Mark – Banner Ads</title>
<link rel="stylesheet" href="https://fonts.googleapis.com/css2?family=Montserrat:wght@700;800;900&display=swap">
<style>
  :root {
    --stage: #8a8a8a;
    --green-deep: #3c9b3e;
    --green-main: #45a645;
    --green-bright: #52b152;
    --green-light: #c6f5a7;
    --gold: #e8c777;
    --red: #e5252a;
    --white: #ffffff;
    --cover-top: #fbfbfb;
    --cover-bottom: #e4e4e4;
  }
  * { box-sizing: border-box; margin: 0; padding: 0; }
  html, body {
    width: 1200px; height: 870px; overflow: hidden;
    background: var(--stage);
    font-family: "Montserrat", Arial, sans-serif;
  }
  .canvas { position: relative; width: 1200px; height: 870px; }

  .banner { position: absolute; overflow: hidden; background: var(--green-main); color: var(--white); }
  .banner-bg { position: absolute; inset: 0; width: 100%; height: 100%; }
  .banner-copy { position: absolute; text-align: center; font-weight: 800; }
  .headline { line-height: 1; text-shadow: 2px 2px 0 rgba(20, 90, 25, .45); }
  .headline > span { display: block; }
  .headline .lead { font-weight: 800; }
  .headline .big { font-weight: 900; letter-spacing: -0.01em; }
  .headline .article { display: inline; font-size: .45em; margin-right: .1em; }
  .subline { font-weight: 800; }
  .cta {
    display: block; background: var(--red); color: var(--white);
    border: 2px solid var(--white); border-radius: 999px;
    font-weight: 800; text-decoration: none; text-align: center;
  }
  .product-shot {
    position: absolute; border-radius: 6px;
    background: linear-gradient(160deg, var(--cover-top), var(--cover-bottom));
    box-shadow: 0 6px 14px rgba(0,0,0,.18);
  }

  /* Leaderboard */
  .banner-wide { left: 73px; top: 403px; width: 827px; height: 340px; }
  .banner-wide .banner-copy { left: 20px; top: 28px; width: 430px; }
  .banner-wide .lead { font-size: 38px; }
  .banner-wide .big { font-size: 70px; }
  .banner-wide .lead + .big { margin-top: -4px; }
  .banner-wide .subline { font-size: 22.5px; line-height: 29px; margin-top: 10px; letter-spacing: -0.005em; }
  .banner-wide .cta { width: 292px; height: 38px; line-height: 34px; font-size: 21px; margin: 4px auto 0; }
  .banner-wide .product-shot { left: 450px; top: 27px; width: 330px; height: 287px; }

  /* Skyscraper */
  .banner-tall { left: 945px; top: 115px; width: 180px; height: 628px; }
  .banner-tall .banner-copy { left: 0; top: 62px; width: 180px; }
  .banner-tall .lead { font-size: 20px; }
  .banner-tall .big { font-size: 35px; }
  .banner-tall .subline { font-size: 15px; line-height: 20px; margin-top: 30px; }
  .banner-tall .cta { width: 150px; height: 20px; line-height: 16px; font-size: 11px; margin: 18px auto 0; }
  .banner-tall .product-shot { left: 7px; top: 361px; width: 166px; height: 142px; }
</style>
</head>
<body>
<main class="canvas">

  <section class="banner banner-wide" aria-label="Leaderboard banner">
    <svg class="banner-bg" viewBox="0 0 827 340" preserveAspectRatio="none" aria-hidden="true">
      <polygon points="0,0 420,0 190,340 0,340" fill="var(--green-bright)"/>
      <polygon points="410,0 467,0 617,340 380,340" fill="var(--green-deep)"/>
      <polygon points="410,0 467,0 560,140 520,150" fill="var(--gold)" opacity=".9"/>
      <polygon points="467,0 827,0 827,340 617,340" fill="var(--green-light)"/>
    </svg>
    <div class="banner-copy">
      <h2 class="headline">
        <span class="lead">Need to</span>
        <span class="big">Remove</span>
        <span class="big"><span class="article">a</span>CCJ?</span>
      </h2>
      <p class="subline">Find out how with this simple<br>jargon-free guide</p>
      <a class="cta" href="https://clearyourrecordguide.co.uk/">Get Your Copy Now</a>
    </div>
    <div class="product-shot" role="img" aria-label="Paperback, tablet and phone editions of the guide Clearing a Court Debt Mark"></div>
  </section>

  <section class="banner banner-tall" aria-label="Skyscraper banner">
    <svg class="banner-bg" viewBox="0 0 180 628" preserveAspectRatio="none" aria-hidden="true">
      <polygon points="0,0 180,0 180,300 0,240" fill="var(--green-bright)"/>
      <polygon points="0,230 0,316 180,440 180,360" fill="var(--green-deep)"/>
      <polygon points="0,230 0,290 40,300 25,255" fill="var(--gold)" opacity=".9"/>
      <polygon points="0,316 180,440 180,628 0,628" fill="var(--green-light)"/>
      <polygon points="110,470 180,500 180,580" fill="var(--green-deep)" opacity=".85"/>
    </svg>
    <div class="banner-copy">
      <h2 class="headline">
        <span class="lead">Need to</span>
        <span class="big">Remove</span>
        <span class="big"><span class="article">a</span>CCJ?</span>
      </h2>
      <p class="subline">Find out how<br>with this simple<br>jargon-free<br>guide</p>
      <a class="cta" href="https://clearyourrecordguide.co.uk/">Get Your Copy Now</a>
    </div>
    <div class="product-shot" role="img" aria-label="Paperback, tablet and phone editions of the guide Clearing a Court Debt Mark"></div>
  </section>

</main>
</body>
</html>
```